Dog care service needs business card design

Our company is Pawsome Haven. We provide care for dogs while their owners are away, either through home visits or a holiday stay in the homes of carefully selected minders. Our existing website & Chatterbook cover should provide all the colour cues for our business cards - namely blues, blondes and grey. We have an existing logo (provided).

www.pawsomehaven-demo.com.au
www.facebook.com/pawsomehavenau

We wish to clearly communicate our three areas of service "dog minding, home visits, dog walking".

We would like to have the files ready for upload to Prontoprint (or similar) for immediate printing.

Target Market(s)

Dog owners who love their dogs like family

Industry/Entity Type

Business

Contact Information for Business Card

Pawsome Haven
Ph: 0491 574 318

Font styles to use
Sans Serif

Colors
33a6d7
3176b5

Requirements
Must have
• Logo
• Telephone number
• website
• "Dog minding, home visits, dog walking"
Should not have
• any additional illustrations beyond the logo.

```html
<!DOCTYPE html>
<html lang="en">
<head>
<meta charset="utf-8">
<title>Pawsome Haven – Business Card</title>
<link rel="stylesheet" href="https://fonts.googleapis.com/css2?family=Cinzel:wght@400;700&family=Nunito:wght@800&display=swap">
<style>
  :root {
    --backdrop: #e9e6e1;
    --card-light: #f4f6f8;
    --card-mist: #dfe5ea;
    --slate-dark: #2b3848;
    --slate-mid: #3e4d60;
    --brand-blue: #3176b5;
    --brand-sky: #33a6d7;
    --ink-grey: #6a7380;
    --ink-dark: #3b4450;
    --white: #ffffff;
    --photo-blonde: #c9944f;
    --photo-shade: #3d4a5a;
    --photo-sky: #a9c3d9;
  }
  * { box-sizing: border-box; margin: 0; padding: 0; }
  html, body { width: 1200px; height: 600px; overflow: hidden; }
  body {
    background: var(--backdrop);
    font-family: "Cinzel", Georgia, serif;
    position: relative;
  }
  .card {
    position: absolute;
    top: 157px;
    width: 500px;
    height: 286px;
    border-radius: 16px;
    overflow: hidden;
    box-shadow: 0 10px 26px rgba(0,0,0,.22);
  }

  /* Front */
  .card-front {
    left: 60px;
    background: linear-gradient(120deg, var(--card-light) 0%, var(--white) 45%, var(--card-mist) 100%);
  }
  .front-photo {
    position: absolute;
    top: 0; right: 0;
    width: 178px; height: 100%;
    background: linear-gradient(160deg, var(--photo-sky) 0%, var(--photo-blonde) 45%, var(--photo-shade) 100%);
  }
  .front-stripe {
    position: absolute;
    top: 0; right: 178px;
    width: 7px; height: 100%;
    background: linear-gradient(180deg, var(--brand-sky), var(--brand-blue));
  }
  .front-content {
    position: absolute;
    left: 30px; top: 28px;
    width: 270px;
  }
  .brand {
    display: flex;
    align-items: center;
    gap: 10px;
    margin-bottom: 26px;
  }
  .brand-dot {
    width: 34px; height: 34px;
    border-radius: 50%;
    background: var(--slate-dark);
    flex: none;
  }
  .brand-name {
    font-family: "Cinzel", Georgia, serif;
    font-weight: 700;
    font-size: 25px;
    line-height: 1;
    color: var(--slate-dark);
  }
  .holder-name {
    font-weight: 700;
    font-size: 17px;
    color: var(--brand-blue);
    letter-spacing: .5px;
  }
  .holder-role {
    font-size: 10px;
    color: var(--ink-grey);
    letter-spacing: 1px;
    margin-bottom: 18px;
  }
  .address {
    font-size: 10px;
    line-height: 1.45;
    color: var(--ink-grey);
    margin-bottom: 14px;
  }
  .contact-list { list-style: none; }
  .contact-list li {
    display: flex;
    align-items: center;
    gap: 8px;
    font-size: 10px;
    color: var(--ink-dark);
    line-height: 1.8;
  }
  .contact-icon { width: 12px; height: 12px; flex: none; }

  /* Back */
  .card-back {
    left: 640px;
    background: linear-gradient(135deg, var(--slate-mid) 0%, var(--slate-dark) 100%);
    color: var(--white);
  }
  .back-content {
    position: absolute;
    inset: 0;
    display: flex;
    flex-direction: column;
    align-items: center;
    justify-content: center;
    text-align: center;
  }
  .back-brand {
    display: flex;
    align-items: center;
    gap: 12px;
    margin-bottom: 24px;
  }
  .back-brand .brand-dot { background: var(--white); width: 40px; height: 40px; }
  .back-brand .brand-name { color: var(--white); font-size: 30px; }
  .services-title {
    font-weight: 700;
    font-size: 14px;
    letter-spacing: 1.5px;
    margin-bottom: 8px;
  }
  .services-list {
    font-size: 11px;
    letter-spacing: 1px;
    color: #dbe3ec;
  }
</style>
</head>
<body>

  <section class="card card-front">
    <div class="front-content">
      <div class="brand">
        <span class="brand-dot"></span>
        <span class="brand-name">Pawsome Haven</span>
      </div>
      <p class="holder-name">Pawsome Haven</p>
      <p class="holder-role">Founder/CEO</p>
      <p class="address">Elmwood Vale, New South Wales<br>Australia 2999</p>
      <ul class="contact-list">
        <li>
          <svg class="contact-icon" viewBox="0 0 12 12" aria-hidden="true">
            <rect width="12" height="12" rx="2" fill="#3176b5"/>
            <path d="M3.5 2.5 L5 2.5 L5.5 4.5 L4.6 5.2 Q5.5 7 6.8 7.4 L7.5 6.5 L9.5 7 L9.5 8.5 Q6 9.5 3 4.5 Z" fill="#fff"/>
          </svg>
          0491 574 318
        </li>
        <li>
          <svg class="contact-icon" viewBox="0 0 12 12" aria-hidden="true">
            <rect width="12" height="12" rx="2" fill="#3176b5"/>
            <rect x="2.5" y="3.5" width="7" height="5" fill="none" stroke="#fff" stroke-width="1"/>
            <path d="M2.5 3.5 L6 6.5 L9.5 3.5" fill="none" stroke="#fff" stroke-width="1"/>
          </svg>
          info@pawsomehaven-demo.com.au
        </li>
        <li>
          <svg class="contact-icon" viewBox="0 0 12 12" aria-hidden="true">
            <rect width="12" height="12" rx="2" fill="#3176b5"/>
            <circle cx="6" cy="6" r="3.3" fill="none" stroke="#fff" stroke-width="1"/>
            <path d="M2.7 6 H9.3 M6 2.7 Q4.3 6 6 9.3 M6 2.7 Q7.7 6 6 9.3" fill="none" stroke="#fff" stroke-width=".8"/>
          </svg>
          www.pawsomehaven-demo.com.au
        </li>
      </ul>
    </div>
    <div class="front-stripe"></div>
    <div class="front-photo" role="img" aria-label="Photo of a golden retriever puppy looking out of a car window"></div>
  </section>

  <section class="card card-back">
    <div class="back-content">
      <div class="back-brand">
        <span class="brand-dot"></span>
        <span class="brand-name">Pawsome Haven</span>
      </div>
      <p class="services-title">Our Services</p>
      <p class="services-list">Dog Minding | Home Visits | Dog Walking</p>
    </div>
  </section>

</body>
</html>
```